mental health business card

Double sided business card with logo on front and practitioners details on back.
The front of card should be while and back either blue or grey to match logo.

Space on back for appointment date and time to be written.

Please note that details are not available yet for address etc as currently moving 4500km across Australia. Just use generic or old info from attached letterhead.
Updates

Dear Designers,

Please note business card is also appointment card must have area where  date and time of clients next appointment can be written in.

Target Market(s)

This is card for patients and colleagues

Industry/Entity Type

Mental Health

Requirements
Must have
• Name
Director / Clinical Psychologist
email
web
phone
phone

Nice to have
• embossing on front of card

```html
<!DOCTYPE html>
<html lang="en">
<head>
<meta charset="utf-8">
<title>Harbourlight Wellbeing – Business &amp; Appointment Card</title>
<link rel="stylesheet" href="https://fonts.googleapis.com/css2?family=Open+Sans:ital,wght@0,400;0,600;0,700;1,600&display=swap">
<style>
  :root {
    --stage: #d6d8da;
    --paper: #ffffff;
    --navy: #124a6b;
    --navy-deep: #0f3f5c;
    --sky: #14aee8;
    --sky-mid: #0a86c0;
    --rule: #6f8fa3;
    --grey-text: #7a7a7a;
    --white: #ffffff;
  }
  * { box-sizing: border-box; margin: 0; padding: 0; }
  html, body {
    width: 1200px; height: 900px; overflow: hidden;
    background: var(--stage);
    font-family: "Open Sans", Arial, sans-serif;
  }
  .stage { position: relative; width: 1200px; height: 900px; }

  .card {
    position: absolute;
    width: 540px; height: 310px;
    background: var(--paper);
    border-radius: 14px;
    overflow: hidden;
    box-shadow: 0 6px 18px rgba(0,0,0,0.18);
  }
  .card--appointment { left: 40px; top: 295px; }
  .card--contact { left: 620px; top: 295px; }
  .card__art { position: absolute; inset: 0; width: 100%; height: 100%; }

  /* Appointment side */
  .appointment__title {
    position: absolute; left: 170px; top: 42px;
    font-size: 16px; font-weight: 700; color: var(--navy);
  }
  .appointment__line {
    position: absolute; left: 170px; width: 340px; height: 0;
    border-top: 1.5px solid var(--rule);
  }

  /* Wordmark */
  .wordmark { position: absolute; display: flex; align-items: center; gap: 12px; }
  .wordmark__square { width: 46px; height: 46px; }
  .wordmark__name {
    font-weight: 600; line-height: 1.05; letter-spacing: 0.5px;
    text-transform: uppercase;
  }
  .wordmark--light { left: 30px; bottom: 26px; }
  .wordmark--light .wordmark__square { background: var(--white); }
  .wordmark--light .wordmark__name { color: var(--white); font-size: 22px; }
  .wordmark--dark { left: 30px; top: 28px; }
  .wordmark--dark .wordmark__square { background: var(--navy); width: 56px; height: 56px; }
  .wordmark--dark .wordmark__name { color: var(--navy); font-size: 28px; }

  /* Contact side */
  .company {
    position: absolute; left: 34px; top: 198px;
    font-size: 12.5px; line-height: 17px; color: var(--white);
  }
  .company__label { color: var(--sky); font-style: italic; font-weight: 600; }
  .company__name { color: var(--sky); font-style: italic; font-weight: 600; }
  .company__address { text-transform: uppercase; }

  .practitioner { position: absolute; left: 360px; top: 178px; color: var(--white); }
  .practitioner__name {
    color: var(--sky); font-weight: 700; font-size: 15px; text-transform: uppercase;
  }
  .practitioner__role { font-size: 12px; }

  .contact-list {
    position: absolute; left: 346px; top: 245px; list-style: none;
    font-size: 12.5px; line-height: 18px; color: var(--white);
  }
  .contact-list__item { display: flex; align-items: center; gap: 7px; }
  .contact-list__icon { width: 12px; height: 12px; flex: none; }
</style>
</head>
<body>
<main class="stage">

  <!-- Appointment side -->
  <section class="card card--appointment" aria-label="Appointment side">
    <svg class="card__art" viewBox="0 0 540 310" aria-hidden="true">
      <defs>
        <linearGradient id="swoosh-a" x1="0" y1="0" x2="1" y2="0">
          <stop offset="0" stop-color="#124a6b"/>
          <stop offset="0.55" stop-color="#0a86c0"/>
          <stop offset="1" stop-color="#14aee8"/>
        </linearGradient>
      </defs>
      <path d="M0,105 C150,215 360,228 540,195 L540,310 L0,310 Z" fill="url(#swoosh-a)"/>
      <path d="M0,120 C150,232 350,258 540,245 L540,310 L0,310 Z" fill="#124a6b"/>
    </svg>
    <p class="appointment__title">Appointment Details:</p>
    <span class="appointment__line" style="top:82px"></span>
    <span class="appointment__line" style="top:116px"></span>
    <span class="appointment__line" style="top:150px"></span>
    <div class="wordmark wordmark--light">
      <span class="wordmark__square"></span>
      <span class="wordmark__name">Harbourlight<br>Wellbeing</span>
    </div>
  </section>

  <!-- Contact side -->
  <section class="card card--contact" aria-label="Contact side">
    <svg class="card__art" viewBox="0 0 540 310" aria-hidden="true">
      <defs>
        <linearGradient id="swoosh-b" x1="0" y1="0" x2="1" y2="0">
          <stop offset="0" stop-color="#124a6b"/>
          <stop offset="0.6" stop-color="#0a86c0"/>
          <stop offset="1" stop-color="#0e9fd8"/>
        </linearGradient>
      </defs>
      <path d="M0,148 C220,150 430,118 540,45 L540,310 L0,310 Z" fill="url(#swoosh-b)"/>
      <path d="M0,160 C220,166 440,138 540,78 L540,310 L0,310 Z" fill="#124a6b"/>
    </svg>

    <div class="wordmark wordmark--dark">
      <span class="wordmark__square"></span>
      <span class="wordmark__name">Harbourlight<br>Wellbeing</span>
    </div>

    <div class="company">
      <p><span class="company__label">ABN:</span> 41 208 664 917</p>
      <p><span class="company__label">ACN:</span> 208664917</p>
      <p class="company__name">Harbourlight Wellbeing Services Pty Ltd.</p>
      <p class="company__address">24 Wattle Court, Lakeside 6105</p>
    </div>

    <div class="practitioner">
      <p class="practitioner__name">Maren Ellis</p>
      <p class="practitioner__role">Director / Clinical Psychologist</p>
    </div>

    <ul class="contact-list">
      <li class="contact-list__item">
        <svg class="contact-list__icon" viewBox="0 0 12 12" aria-hidden="true"><circle cx="6" cy="6" r="6" fill="#14aee8"/><path d="M3.6,3 L5,3.2 L5.3,4.6 L4.6,5.1 C5,6 5.8,6.8 6.8,7.3 L7.3,6.6 L8.7,6.9 L8.9,8.3 C6,8.7 3.2,6 3.6,3 Z" fill="#124a6b"/></svg>
        (08) 5550 1842
      </li>
      <li class="contact-list__item">
        <svg class="contact-list__icon" viewBox="0 0 12 12" aria-hidden="true"><circle cx="6" cy="6" r="6" fill="#14aee8"/><rect x="3" y="4" width="6" height="4.2" fill="#124a6b"/><path d="M3,4 L6,6.3 L9,4" fill="none" stroke="#14aee8" stroke-width="0.7"/></svg>
        mellis@hlw.net.au
      </li>
      <li class="contact-list__item">
        <svg class="contact-list__icon" viewBox="0 0 12 12" aria-hidden="true"><circle cx="6" cy="6" r="5.3" fill="none" stroke="#14aee8" stroke-width="1.2"/><ellipse cx="6" cy="6" rx="2.2" ry="5.3" fill="none" stroke="#14aee8" stroke-width="0.9"/><line x1="0.8" y1="6" x2="11.2" y2="6" stroke="#14aee8" stroke-width="0.9"/></svg>
        www.hlw.net.au
      </li>
    </ul>
  </section>

</main>
</body>
</html>
```